Lanternfield Drinks business cards

We need a business card design for our new logo. The company is modern, progressive, professional, yet approachable. The key products are ready to drink bottles and cans of coffee based beverages.
These cards will be a critical part of the first impression made by our sales organization, business development team, and all external facing personnel.
Card can be a vertical or horizontal orientation.

Target Market(s)

Customers, suppliers, business partners

Industry/Entity Type

Business

Contact Information for Business Card

Business cards should feature Company Name and Logo.

Font styles to use
Serif

Colors

Designer to choose colors to be used in the design.

Requirements
Must have
• Strong readability of Name, phone #, mobile number and email address.
• Job title, website url, Street Address, and other details can be secondary level readability.
Nice to have
• High impact, simplistic quality design.
• Ok to utilize the 'H in the box' separate from the company name

```html
<!DOCTYPE html>
<html lang="en">
<head>
<meta charset="utf-8">
<title>Lanternfield Drinks business cards</title>
<link href="https://fonts.googleapis.com/css2?family=Lora:wght@400;700&display=swap" rel="stylesheet">
<style>
  :root {
    --orange: #e85a2c;
    --orange-deep: #d44a20;
    --ink: #3a3a3a;
    --grey: #9a9a9a;
    --paper: #ffffff;
    --backdrop: #a9a9a9;
  }
  * { box-sizing: border-box; margin: 0; padding: 0; }
  html, body { width: 1200px; height: 900px; overflow: hidden; }
  body {
    background: var(--backdrop);
    font-family: "Lora", Georgia, serif;
    position: relative;
  }
  .card {
    position: absolute;
    width: 620px;
    height: 354px;
    border-radius: 22px;
    overflow: hidden;
    box-shadow: 0 10px 24px rgba(0,0,0,0.25);
  }
  .card-front {
    left: 80px; top: 70px;
    background: linear-gradient(135deg, var(--orange-deep), var(--orange));
    display: flex; align-items: center; justify-content: center;
  }
  .card-back {
    left: 500px; top: 476px;
    background: linear-gradient(160deg, #ffffff, #f0f0f0);
  }
  .brand { display: flex; align-items: center; gap: 14px; }
  .brand-square {
    width: 52px; height: 52px;
    border: 5px solid currentColor;
    flex: none;
  }
  .brand-name {
    font-weight: 700;
    font-size: 34px;
    letter-spacing: 1px;
    text-transform: uppercase;
    white-space: nowrap;
  }
  .card-front .brand { color: var(--paper); }
  .card-back .brand { color: var(--orange); position: absolute; left: 36px; top: 40px; gap: 12px; }
  .card-back .brand-square { width: 40px; height: 40px; border-width: 4px; }
  .card-back .brand-name { font-size: 24px; }
  .swoosh { position: absolute; inset: 0; }
  .rule-top {
    position: absolute; left: 250px; right: 26px; top: 106px;
    height: 1px; background: var(--grey);
  }
  .address {
    position: absolute; right: 30px; top: 116px;
    text-align: right; font-size: 14px; color: var(--ink); line-height: 1.4;
  }
  .person { position: absolute; left: 70px; top: 124px; }
  .person-name { font-size: 30px; font-weight: 700; color: var(--orange); line-height: 1.2; }
  .person-title { font-size: 18px; color: var(--ink); }
  .rule-contact {
    position: absolute; left: 70px; top: 204px;
    width: 220px; height: 1px; background: var(--grey);
  }
  .contacts {
    position: absolute; left: 70px; top: 214px;
    list-style: none; font-size: 15px; color: var(--ink);
  }
  .contacts li { display: flex; align-items: center; gap: 8px; margin-bottom: 6px; }
  .contacts svg { width: 14px; height: 14px; fill: var(--orange); }
  .website {
    position: absolute; right: 28px; top: 234px;
    font-size: 13px; color: var(--paper);
  }
</style>
</head>
<body>
  <section class="card card-front">
    <div class="brand">
      <span class="brand-square"></span>
      <span class="brand-name">Lanternfield Drinks</span>
    </div>
  </section>

  <section class="card card-back">
    <svg class="swoosh" viewBox="0 0 620 354" preserveAspectRatio="none" aria-hidden="true">
      <path d="M260 354 C320 240 400 190 620 172 L620 354 Z" fill="#8c8c8c"/>
      <path d="M272 354 C332 242 410 193 620 180 L620 354 Z" fill="#ffffff"/>
      <path d="M282 354 C342 244 420 196 620 186 L620 354 Z" fill="var(--orange)"/>
    </svg>
    <div class="brand">
      <span class="brand-square"></span>
      <span class="brand-name">Lanternfield Drinks</span>
    </div>
    <div class="rule-top"></div>
    <p class="address">Level 2, 17 Harbor Lane<br>Ashford, VIC 3100</p>
    <div class="person">
      <h1 class="person-name">Adrian Kell</h1>
      <p class="person-title">President</p>
    </div>
    <div class="rule-contact"></div>
    <ul class="contacts">
      <li>
        <svg viewBox="0 0 24 24"><path d="M6.6 10.8a15 15 0 0 0 6.6 6.6l2.2-2.2a1 1 0 0 1 1-.25 11.4 11.4 0 0 0 3.6.57 1 1 0 0 1 1 1V20a1 1 0 0 1-1 1A17 17 0 0 1 3 4a1 1 0 0 1 1-1h3.5a1 1 0 0 1 1 1c0 1.25.2 2.45.57 3.57a1 1 0 0 1-.25 1z"/></svg>
        555 210 4836
      </li>
      <li>
        <svg viewBox="0 0 24 24"><path d="M2 5h20v14H2z M2 5l10 8 10-8" stroke="#fff" stroke-width="1.5"/></svg>
        info@lanternfielddrinks.com
      </li>
    </ul>
    <p class="website">www.lanternfielddrinks.com</p>
  </section>
</body>
</html>
```